Business card design to suit our website

Need a nice looking business card for our business based off images from our Website and provided images. The business card will require 2 different names (for the 2 owners). The business card should include images from our website, facebook (keel bracket works set) or the pictures provided. it should also contain all contact information.
Our website is www.keelbracketworks.com.au
Please dont use image from top bar of website. If images are used please use the ones of our product under the buy it now tab

Target Market(s)

Automotive

Industry/Entity Type

Automotive Part

Contact Information for Business Card

Business Name. contact details including names phone number email. logo
2 business cards needed with 2 different persons names and phone number.

Colors

Designer to choose colors to be used in the design.

Requirements
Must have
• whatever looks best

```html
<!DOCTYPE html>
<html lang="en">
<head>
<meta charset="utf-8">
<title>Steadfast Bracket Set – Business Cards</title>
<link rel="stylesheet" href="https://fonts.googleapis.com/css2?family=Open+Sans:wght@400;600;700;800&display=swap">
<style>
  :root {
    --stage: #2a2a2c;
    --card-light: #f4f4f5;
    --card-mid: #d9d9dc;
    --tread-light: #e2e2e4;
    --tread-dark: #a9a9ad;
    --brand-red: #a3141c;
    --brand-red-dark: #7e0d13;
    --ink: #1e1e1e;
    --ink-soft: #3a3a3a;
    --band-black: #111111;
    --seal-gold: #c9a03c;
    --seal-dark: #2b2416;
    --white: #ffffff;
  }
  * { box-sizing: border-box; margin: 0; padding: 0; }
  html, body { width: 1200px; height: 900px; overflow: hidden; }
  body {
    background: var(--stage);
    font-family: "Open Sans", Arial, sans-serif;
    position: relative;
  }
  .card {
    position: absolute;
    border-radius: 26px;
    overflow: hidden;
    background: linear-gradient(160deg, var(--card-light) 0%, var(--card-mid) 100%);
    box-shadow: 0 10px 30px rgba(0,0,0,.45);
  }
  /* front */
  .card--front { left: 340px; top: 50px; width: 520px; height: 300px; }
  .card--front .tread-band {
    position: absolute; left: 0; right: 0; top: 78px; height: 112px;
    background: linear-gradient(180deg, var(--tread-light), #ececee 50%, var(--tread-light));
  }
  .card--front .brand {
    position: absolute; left: 70px; top: 108px;
    display: flex; align-items: center; gap: 10px;
    white-space: nowrap;
  }
  .card--front .brand-dot {
    width: 20px; height: 20px; border-radius: 50%; background: var(--brand-red); flex: none;
  }
  .card--front .brand-name {
    font-size: 30px; font-weight: 800; color: var(--brand-red); letter-spacing: -0.3px; line-height: 1.2;
  }
  .seal {
    position: absolute; right: 28px; top: 150px; width: 96px; height: 96px;
    border-radius: 50%;
    background: radial-gradient(circle, var(--seal-dark) 55%, var(--seal-gold) 57%);
    z-index: 2;
  }
  .black-stripe {
    position: absolute; left: 0; right: 0; top: 212px; height: 12px; background: var(--band-black);
  }
  .red-band {
    position: absolute; left: 0; right: 0; top: 224px; bottom: 0;
    background: linear-gradient(180deg, var(--brand-red), var(--brand-red-dark));
    display: flex; align-items: center; justify-content: center;
  }
  .web-address { color: var(--white); font-weight: 700; font-size: 17px; padding-right: 60px; white-space: nowrap; }

  /* back */
  .card--back { width: 540px; height: 320px; top: 420px; }
  .card--jane { left: 40px; }
  .card--john { left: 620px; }
  .card--back .tread-band {
    position: absolute; left: 0; right: 0; top: 0; height: 110px;
    background: linear-gradient(180deg, var(--tread-dark), var(--tread-light));
  }
  .card--back .brand {
    position: absolute; top: 40px; left: 0; right: 0;
    display: flex; justify-content: center; align-items: center; gap: 8px; white-space: nowrap;
  }
  .card--back .brand-dot { width: 14px; height: 14px; border-radius: 50%; background: var(--brand-red); flex: none; }
  .card--back .brand-name { font-size: 26px; font-weight: 800; color: var(--brand-red); }
  .person { position: absolute; top: 138px; left: 0; right: 0; text-align: center; color: var(--ink); }
  .person-name { font-size: 17px; font-weight: 700; }
  .person-role { font-weight: 400; font-size: 14px; }
  .email { margin-top: 4px; font-size: 13px; display: flex; justify-content: center; align-items: center; gap: 6px; }
  .contact { position: absolute; top: 222px; display: flex; gap: 8px; color: var(--ink-soft); font-size: 15px; line-height: 1.4; white-space: nowrap; }
  .contact--address { left: 50px; }
  .contact--phones { left: 340px; }
  .phone-line { display: flex; align-items: center; gap: 8px; }
  svg.icon { flex: none; fill: var(--brand-red); }
</style>
</head>
<body>

<section class="card card--front">
  <div class="tread-band" role="img" aria-label="Tyre tread pattern band"></div>
  <div class="brand"><span class="brand-dot"></span><span class="brand-name">Steadfast Bracket Set</span></div>
  <div class="seal" role="img" aria-label="Warranty seal"></div>
  <div class="black-stripe"></div>
  <div class="red-band"><span class="web-address">www.keelbracketworks.com.au</span></div>
</section>

<section class="card card--back card--jane">
  <div class="tread-band" role="img" aria-label="Tyre tread pattern band"></div>
  <div class="brand"><span class="brand-dot"></span><span class="brand-name">Steadfast Bracket Set</span></div>
  <div class="person">
    <div class="person-name">Mara Quill <span class="person-role">| Owner</span></div>
    <div class="email">
      <svg class="icon" width="14" height="10" viewBox="0 0 14 10"><path d="M0 0h14v10H0z M1 1l6 4 6-4" /></svg>
      maraquill@keelbracketworks.com.au
    </div>
  </div>
  <div class="contact contact--address">
    <svg class="icon" width="14" height="18" viewBox="0 0 14 18"><path d="M7 0a7 7 0 0 1 7 7c0 5-7 11-7 11S0 12 0 7a7 7 0 0 1 7-7zm0 4a3 3 0 1 0 0 6 3 3 0 0 0 0-6z"/></svg>
    <div>412 Harbour Line Rd.<br>Unit 7, Box 22<br>Portside, VIC 3999</div>
  </div>
  <div class="contact contact--phones">
    <div>
      <div class="phone-line"><svg class="icon" width="14" height="14" viewBox="0 0 14 14"><path d="M3 0l3 3-2 2a8 8 0 0 0 5 5l2-2 3 3-2 3C6 14 0 8 0 2z"/></svg>1300 482 170</div>
      <div class="phone-line"><svg class="icon" width="14" height="16" viewBox="0 0 10 16"><path d="M1 0h8a1 1 0 0 1 1 1v14a1 1 0 0 1-1 1H1a1 1 0 0 1-1-1V1a1 1 0 0 1 1-1zm1 2v9h6V2z"/></svg>0400 261 358</div>
    </div>
  </div>
</section>

<section class="card card--back card--john">
  <div class="tread-band" role="img" aria-label="Tyre tread pattern band"></div>
  <div class="brand"><span class="brand-dot"></span><span class="brand-name">Steadfast Bracket Set</span></div>
  <div class="person">
    <div class="person-name">Owen Quill <span class="person-role">| Owner</span></div>
    <div class="email">
      <svg class="icon" width="14" height="10" viewBox="0 0 14 10"><path d="M0 0h14v10H0z M1 1l6 4 6-4" /></svg>
      owenquill@keelbracketworks.com.au
    </div>
  </div>
  <div class="contact contact--address">
    <svg class="icon" width="14" height="18" viewBox="0 0 14 18"><path d="M7 0a7 7 0 0 1 7 7c0 5-7 11-7 11S0 12 0 7a7 7 0 0 1 7-7zm0 4a3 3 0 1 0 0 6 3 3 0 0 0 0-6z"/></svg>
    <div>412 Harbour Line Rd.<br>Unit 7, Box 22<br>Portside, VIC 3999</div>
  </div>
  <div class="contact contact--phones">
    <div>
      <div class="phone-line"><svg class="icon" width="14" height="14" viewBox="0 0 14 14"><path d="M3 0l3 3-2 2a8 8 0 0 0 5 5l2-2 3 3-2 3C6 14 0 8 0 2z"/></svg>1300 482 170</div>
      <div class="phone-line"><svg class="icon" width="14" height="16" viewBox="0 0 10 16"><path d="M1 0h8a1 1 0 0 1 1 1v14a1 1 0 0 1-1 1H1a1 1 0 0 1-1-1V1a1 1 0 0 1 1-1zm1 2v9h6V2z"/></svg>0400 261 358</div>
    </div>
  </div>
</section>

</body>
</html>
```